Website redesign for Law Firm

Looking for someone experienced in Wordpress to redesign our existing website as part of a rebrand. The scope of the redesign includes:

1. Change logo and colours throughout to match new name and branding (minimal pink, mainly light and dark blue)
2. Redesign to focus of converison rate optimisation and modernisation. The focus is conveyancing and the call to action is Request an Instant Quote
3. Remove Meet the Leadership Team section from homepage
4. Remove Meet the Team section from About Us Page
5. Change ribbon to have Special Conditions and Blog as their own tabs, not a drop down under Resources
6. Include a Get a Free Quote section on the homepage similar to deedmarkhub.com.au, however does not require a State section. This calculator is to be coded into the final design and there will only be 3 different prices depending on what they choose

SLUG/Page stucture must stay the same for the final coded design.

Wanting something that is very clean and conversion rate optimised.

The existing website is tellerbyfirm.com.au. It is moving to harbourlinetitlelegal.com.au and changing name to Harbourline Title Legal.

The logo design files can be found here: https://files.examplevault.net/share/9kQpLr2XwTz7Bv4Nm8HcYd3Fs6Gj1?view=open

The colour codes and font name are included there also. You must use the correct colour codes from the logo. You can add a lighter blue to be the contract colour also. The pink colour is not to be a main colour it is just a feature colour to be used minimally. The dark blue from the background of the inverse (hex 192330) and a lighter blue are the main colours. Lots of white space and not all a dark background.

Examples of other websites in the industy

- https://keystepsettlements.com/
- https://www.deedmarkhub.com.au/
- https://truelinetransfers.com.au/

Target Market(s)

Professionals buying and selling property

Industry/Entity Type

Legal

Number of Pages Required

5+ page

Colors
0054AA
0677BA
7BADD7
CADEEF
E8F1F8

Requirements
Must have
• Wordpress and Elementor, Blue colour scheme.
Nice to have
• Get creative with the redesign/layout and focus on converison rate, especially above the fold. The existing layout does not need to stay the same
Should not have
• Minimal of the pink

```html
<!DOCTYPE html>
<html lang="en">
<head>
<meta charset="utf-8">
<title>Harbourline Title Legal – Property Lawyers</title>
<link rel="stylesheet" href="https://fonts.googleapis.com/css2?family=Barlow+Semi+Condensed:wght@400;500;600;700&family=Montserrat:wght@400;500;600;700&display=swap">
<style>
:root{
  --blue:#0054aa;
  --blue-mid:#0677ba;
  --blue-soft:#7badd7;
  --blue-pale:#cadeef;
  --blue-mist:#e8f1f8;
  --pink:#e8196d;
  --navy:#192330;
  --navy-2:#2a3544;
  --ink:#192330;
  --text:#5b6070;
  --line:#e3e6ec;
  --field:#f1f4f8;
  --white:#fff;
}
*{box-sizing:border-box;margin:0;padding:0}
html,body{width:1200px;height:4854px;overflow:hidden}
body{position:relative;font-family:"Montserrat",sans-serif;color:var(--ink);background:var(--white)}
.abs{position:absolute}
.head{font-family:"Barlow Semi Condensed",sans-serif;font-weight:400;text-transform:uppercase;color:var(--ink);letter-spacing:.5px}
.hl{font-weight:700;background:linear-gradient(transparent 62%,var(--blue-soft) 62%,var(--blue-soft) 88%,transparent 88%)}
.hl-soft{font-weight:700;background:linear-gradient(transparent 60%,var(--blue-pale) 60%)}
.btn{display:flex;align-items:center;justify-content:center;background:var(--blue);color:#fff;font-family:"Barlow Semi Condensed",sans-serif;font-weight:700;font-size:13px;letter-spacing:.5px;text-transform:uppercase}
.photo{position:absolute}

.hero{position:absolute;left:0;top:0;width:1200px;height:729px;background:linear-gradient(120deg,var(--blue-mist) 0%,#fff 45%,#f3f6fa 100%);overflow:hidden}
.logo-box{position:absolute;left:88px;top:0;width:117px;height:113px;background:var(--navy);display:flex;align-items:center;justify-content:center;text-align:center;color:#fff;font-weight:600;font-size:11px;line-height:1.35;padding:10px}
.nav{position:absolute;top:49px;left:0;font-size:11px;font-weight:500;color:var(--ink)}
.nav span{position:absolute;white-space:nowrap}
.hero-eyebrow{left:88px;top:240px;color:var(--blue-mid);font-size:13px;font-weight:500;text-transform:uppercase}
.hero-title{left:88px;top:268px;font-size:45px;line-height:53px}
.hero-text{left:88px;top:490px;width:420px;font-size:11px;line-height:20px;color:var(--text)}

.about{position:absolute;left:0;top:729px;width:1200px;height:575px;background:var(--navy)}
.about-tag{position:absolute;left:533px;top:83px;width:136px;height:49px;background:var(--navy-2);color:#fff;font-size:13px;font-weight:500;display:flex;align-items:center;justify-content:center}
.about-title{position:absolute;left:0;top:158px;width:1200px;text-align:center;color:#fff;font-size:33px;line-height:41px}
.about-title .hl{color:#fff;background:linear-gradient(transparent 62%,var(--blue-mid) 62%,var(--blue-mid) 88%,transparent 88%)}
.firm-card{position:absolute;left:844px;top:269px;width:305px;height:234px;background:var(--blue);color:#fff;padding:26px 28px}
.firm-card h3{font-family:"Barlow Semi Condensed",sans-serif;font-weight:500;font-size:19px;margin-bottom:12px;text-transform:uppercase}
.firm-card p{font-size:10px;line-height:17px}
.firm-card a{display:inline-block;margin-top:10px;font-size:10px;font-weight:700;text-decoration:underline;color:#fff}

.help-title{left:88px;top:1390px;font-size:35px}
.help-text{left:88px;top:1446px;width:515px;font-size:13px;line-height:22px;color:var(--text)}
.feature{position:absolute;width:330px;display:flex;gap:16px}
.feature .ic{flex:0 0 64px;height:64px;border:1px dashed var(--blue-soft);display:flex;align-items:center;justify-content:center}
.feature .ic i{display:flex;width:50px;height:50px;background:var(--blue);align-items:center;justify-content:center}
.feature .ic i.alt{background:#fff;border:1px solid var(--blue)}
.feature h4{font-size:10.5px;font-weight:600;text-transform:uppercase;margin:2px 0 8px}
.feature p{font-size:10.5px;line-height:17px;color:var(--text)}
.rule{position:absolute;left:64px;width:1072px;height:1px;background:var(--line)}

.sec-title{position:absolute;left:0;width:1200px;text-align:center;font-size:33px}
.quote-band{position:absolute;left:0;top:2308px;width:1200px;height:362px;background:linear-gradient(100deg,var(--blue) 0%,var(--blue-mid) 50%,var(--blue) 100%)}
.svc{position:absolute;top:1990px;height:378px;color:#fff}
.svc .cap{position:absolute;left:0;bottom:0;width:100%;padding:0 26px 34px}
.svc h3{font-family:"Barlow Semi Condensed",sans-serif;font-weight:400;font-size:18px;text-transform:uppercase;line-height:23px}
.svc p{font-size:10px;line-height:15px;margin-top:12px;width:420px}
.quote-title{top:2440px;font-size:58px;font-weight:600;color:#fff;letter-spacing:1px}
.quote-sub{position:absolute;top:2520px;left:0;width:1200px;text-align:center;color:#fff;font-size:16px;font-weight:600}

.ptype{position:absolute;top:2811px;width:101px;height:102px;border:1px dashed #9aa4b2;display:flex;align-items:center;justify-content:center}
.ptype i{display:flex;width:80px;height:80px;background:var(--blue-mist);align-items:center;justify-content:center}
.label{position:absolute;font-size:13px;font-weight:500;text-transform:uppercase;color:var(--ink)}
.field{position:absolute;height:47px;background:var(--field);font-size:11.5px;color:#9a9ca6;display:flex;align-items:center;padding-left:22px}
.when{position:absolute;height:50px;background:var(--blue);color:#fff;font-family:"Barlow Semi Condensed",sans-serif;font-weight:700;font-size:11px;display:flex;align-items:center;justify-content:center;text-transform:uppercase}
.small{position:absolute;font-size:10.5px;line-height:17px;color:var(--text)}

.avatar{position:absolute;background:linear-gradient(160deg,#c9ccd2,#4d5562)}
.arrow{position:absolute;top:3316px;width:34px;height:34px;display:flex;align-items:center;justify-content:center}

.post{position:absolute;top:3792px;width:288px;height:391px;background:#fff;box-shadow:0 4px 18px rgba(0,0,0,.08)}
.post .ph{height:240px}
.post h4{margin:26px 28px 12px;font-size:12px;font-weight:600;text-transform:uppercase;line-height:20px}
.post p{margin:0 28px;font-size:10px;line-height:16px;color:var(--text)}
.post .go{position:absolute;right:28px;bottom:10px;width:30px;height:30px;background:var(--blue);display:flex;align-items:center;justify-content:center}

.footer{position:absolute;left:0;top:4399px;width:1200px;height:455px;background:var(--navy)}
.cta{position:absolute;left:98px;top:4309px;width:1004px;height:128px;background:var(--blue-mid)}
.foot-h{position:absolute;font-family:"Barlow Semi Condensed",sans-serif;font-weight:600;font-size:17px;color:#fff;text-transform:uppercase}
.foot-list{position:absolute;font-size:12px;line-height:26.5px;color:#d7dbe2;list-style:none}
</style>
</head>
<body>

<section class="hero">
  <div class="photo" style="left:520px;top:60px;width:680px;height:669px;background:linear-gradient(180deg,#eef2f7 0%,#b9c6d6 45%,#6f7f94 80%,#d6dbe2 100%)" role="img" aria-label="City skyline with tall glass towers"></div>
  <div class="logo-box">Harbourline Title Legal</div>
  <nav class="nav">
    <span style="left:425px">SERVICES</span>
    <span style="left:497px">SPECIAL CONDITIONS</span>
    <span style="left:631px">BLOG ARTICLES</span>
    <span style="left:733px">ABOUT US</span>
    <span style="left:812px">CONTACT US</span>
  </nav>
  <div class="btn abs" style="left:908px;top:34px;width:204px;height:45px;font-size:11px">Request an instant quote</div>
  <p class="abs hero-eyebrow">We help property</p>
  <div class="photo" style="left:286px;top:218px;width:140px;height:89px;background:linear-gradient(180deg,#a7c1df,#7d8794)" role="img" aria-label="Small city skyline photo"></div>
  <h1 class="abs head hero-title">We help<br>property <span class="hl">developers,</span><br>buyers &amp; sellers<br>like you</h1>
  <p class="abs hero-text">All we do is property law. Rely on our experience to help make your next property transaction a success.</p>
  <div class="btn abs" style="left:88px;top:548px;width:225px;height:47px">Request an instant quote</div>
</section>

<section class="about">
  <div class="about-tag">ABOUT US</div>
  <h2 class="head about-title">Challenging ourselves to bring new<br>and <span class="hl">original ways</span> of thinking</h2>
  <div class="btn abs" style="left:537px;top:269px;width:126px;height:38px;font-size:12px;background:var(--blue-mid)">Learn more</div>
  <div class="abs" style="left:36px;top:222px;width:85px;height:85px;background:#6f7c8e"></div>
  <div class="photo" style="left:64px;top:251px;width:290px;height:252px;background:linear-gradient(180deg,#d4dbe6,#7a8699 60%,#3a414d)" role="img" aria-label="High-rise towers under construction"></div>
  <div class="photo" style="left:401px;top:352px;width:396px;height:151px;background:linear-gradient(90deg,#dfe7ee,#c7d3dc 50%,#a9b8c3)" role="img" aria-label="Model house on architectural plans"></div>
  <div class="photo" style="left:1057px;top:175px;width:143px;height:142px;background:linear-gradient(160deg,#e9ecef,#b6bcc4)" role="img" aria-label="Lawyers meeting at an office desk"></div>
  <div class="firm-card">
    <h3>We are Harbourline</h3>
    <p>Harbourline Title Legal is a specialised property development and conveyancing law firm that is part of the Harbourline Group. This integrated business allows us to offer a one stop shop for all your property law, conveyancing, property development, project marketing and real estate needs.</p>
    <a>READ MORE</a>
  </div>
</section>

<div class="abs" style="left:725px;top:1413px;width:387px;height:100px;background:var(--blue-pale)"></div>
<div class="photo" style="left:780px;top:1381px;width:277px;height:164px;background:linear-gradient(180deg,#8fb4dc,#dfe7f1 45%,#444b58 80%)" role="img" aria-label="Modern dark residential apartment building"></div>
<h2 class="abs head help-title">How can we <span class="hl-soft">help you?</span></h2>
<p class="abs help-text">Harbourline Title Legal is a specialised property development law firm based in Northvale, Brisbane. We provide legal services to property developers for land, unit, house, and townhouse developments of all sizes, as well as conveyancing law services for buyers and sellers.</p>

<div class="feature" style="left:88px;top:1593px">
  <div class="ic"><i><svg width="28" height="28" viewBox="0 0 24 24" fill="none" stroke="#fff" stroke-width="1.5"><rect x="4" y="4" width="16" height="16"/><path d="M8 9h8M8 13h8M8 17h5"/></svg></i></div>
  <div><h4>Development site acquisitions &amp; sales</h4><p>Thorough due diligence and a contract that protects your rights and interests, every time.</p></div>
</div>
<div class="feature" style="left:447px;top:1593px">
  <div class="ic"><i class="alt"><svg width="28" height="28" viewBox="0 0 24 24" fill="none" stroke="#0054aa" stroke-width="1.5"><rect x="5" y="3" width="14" height="18"/><path d="M8 8h8M8 12h8M8 16h5"/></svg></i></div>
  <div><h4>Off the plan contracts</h4><p>Experts in navigating the often complex world of off the plan development contracts.</p></div>
</div>
<div class="feature" style="left:806px;top:1593px">
  <div class="ic"><i><svg width="28" height="28" viewBox="0 0 24 24" fill="none" stroke="#fff" stroke-width="1.5"><path d="M4 8h12l-3-3M20 16H8l3 3"/></svg></i></div>
  <div><h4>Put &amp; call option agreements</h4><p>Whether you're using a put and call option agreement for structuring or to help you on-sell for profit,</p></div>
</div>
<div class="feature" style="left:88px;top:1727px">
  <div class="ic"><i><svg width="28" height="28" viewBox="0 0 24 24" fill="none" stroke="#fff" stroke-width="1.5"><path d="M3 11l9-7 9 7M6 10v10h12V10M10 20v-6h4v6"/></svg></i></div>
  <div><h4>Conveyancing</h4><p>We've helped over 200 people buy and sell their homes in the last 12 months. We have the experience</p></div>
</div>
<div class="feature" style="left:447px;top:1727px">
  <div class="ic"><i class="alt"><svg width="28" height="28" viewBox="0 0 24 24" fill="none" stroke="#0054aa" stroke-width="1.5"><rect x="4" y="4" width="12" height="16"/><path d="M13 15l6-6 2 2-6 6h-2z"/></svg></i></div>
  <div><h4>Joint venture agreements</h4><p>Our JV agreements minimise tax, protect your interests and help you deliver your next property joint venture smoothly.</p></div>
</div>
<div class="feature" style="left:806px;top:1727px">
  <div class="ic"><i><svg width="28" height="28" viewBox="0 0 24 24" fill="none" stroke="#fff" stroke-width="1.5"><path d="M12 3v18M6 7h10l2 2-2 2H6zM18 13H8l-2 2 2 2h10z"/></svg></i></div>
  <div><h4>Titling &amp; structuring advice</h4><p>Not sure what structure to use for your next property development? Tailored structuring advice to suit you.</p></div>
</div>
<div class="rule" style="top:1865px"></div>

<h2 class="head sec-title" style="top:1915px">Our services</h2>
<div class="quote-band"></div>
<article class="svc" style="left:88px;width:588px">
  <div class="photo" style="inset:0;background:linear-gradient(180deg,#aebfd0 0%,#6f7d8c 45%,#1f2a38 100%)" role="img" aria-label="Construction crane over city development site"></div>
  <div class="cap"><h3>Property development lawyers</h3><p>Whether you're experienced in property development or are taking your first steps in this space there's one thing that doesn't change as you move in the property development area:</p></div>
  <div class="abs" style="right:42px;bottom:58px;width:46px;height:46px;background:var(--pink);display:flex;align-items:center;justify-content:center"><svg width="18" height="18" viewBox="0 0 18 18" fill="none" stroke="#fff" stroke-width="1.6"><path d="M4 14L14 4M6 4h8v8"/></svg></div>
</article>
<article class="svc" style="left:697px;width:196px">
  <div class="photo" style="inset:0;background:linear-gradient(180deg,#b4c9e0 0%,#8e9a88 45%,#1f2a38 100%)" role="img" aria-label="Two-storey suburban family home"></div>
  <div class="cap" style="padding:0 26px 36px"><h3 style="font-size:16px">Conveyancing<br>lawyers</h3></div>
</article>
<article class="svc" style="left:914px;width:198px">
  <div class="photo" style="inset:0;background:linear-gradient(180deg,#a9c3e2 0%,#7b8797 50%,#1f2a38 100%)" role="img" aria-label="City towers beside a river bridge"></div>
  <div class="cap" style="padding:0 22px 36px"><h3 style="font-size:16px">Joint venture<br>agreement Brisbane</h3></div>
</article>
<h2 class="head sec-title quote-title">Get a free quote</h2>
<p class="quote-sub">Enter Your Details Below and We'll Calculate Your Conveyancing fees in 30 seconds.</p>
<div class="abs btn" style="left:465px;top:2568px;width:127px;height:38px;background:#fff;color:var(--ink);font-size:12px">BUY</div>
<div class="abs btn" style="left:605px;top:2568px;width:128px;height:38px;background:var(--navy);font-size:12px">SELL</div>

<h2 class="head sec-title" style="top:2744px">What is the <span class="hl-soft">property</span> type?</h2>
<div class="ptype" style="left:183px"><i><svg width="40" height="40" viewBox="0 0 24 24" fill="none" stroke="#192330" stroke-width="1.1"><path d="M3 10l9-6 9 6M5 9v11h14V9M9 20v-5h6v5M8 11h2M14 11h2"/></svg></i></div>
<div class="ptype" style="left:330px"><i><svg width="40" height="40" viewBox="0 0 24 24" fill="none" stroke="#192330" stroke-width="1.1"><path d="M4 8l8-4 8 4v12H4zM8 11h3v3H8zM13 11h3v3h-3zM10 20v-4h4v4"/></svg></i></div>
<div class="ptype" style="left:477px"><i><svg width="40" height="40" viewBox="0 0 24 24" fill="none" stroke="#192330" stroke-width="1.1"><path d="M3 20V8h9v12M12 20V4h9v16M5 11h2M8 11h2M5 15h2M8 15h2M14 8h2M17 8h2M14 12h2M17 12h2"/></svg></i></div>
<div class="ptype" style="left:622px"><i><svg width="40" height="40" viewBox="0 0 24 24" fill="none" stroke="#192330" stroke-width="1.1"><path d="M3 20V9l18-5v16zM6 12h12M6 15h12M6 18h12M10 12v8M14 12v8"/></svg></i></div>
<div class="ptype" style="left:769px"><i><svg width="40" height="40" viewBox="0 0 24 24" fill="none" stroke="#192330" stroke-width="1.1"><path d="M3 20l3-7h12l3 7zM9 4h6v7H9zM12 5.5v4"/></svg></i></div>
<div class="ptype" style="left:916px"><i><svg width="40" height="40" viewBox="0 0 24 24" fill="none" stroke="#192330" stroke-width="1.1"><path d="M4 4h16v16H4zM4 10h6v10M14 4v8h6M10 14h4"/></svg></i></div>

<span class="label" style="left:181px;top:2956px">Your details</span>
<div class="field" style="left:181px;top:2996px;width:194px">First name</div>
<div class="field" style="left:387px;top:2996px;width:192px">Last name</div>
<div class="field" style="left:181px;top:3060px;width:194px">Email address</div>
<div class="field" style="left:387px;top:3060px;width:192px">Phone number</div>
<div class="abs" style="left:183px;top:3124px;width:20px;height:20px;background:var(--blue-pale)"></div>
<p class="small" style="left:214px;top:3120px;width:370px">I agree to receive marketing communications about my property journey from us (Northgate Digital), our related companies and our trusted business partners.-</p>
<div class="abs" style="left:597px;top:2950px;width:1px;height:250px;background:var(--line)"></div>
<span class="label" style="left:622px;top:2956px">When are you planning to buy/sell?</span>
<div class="when" style="left:622px;top:2992px;width:122px">Now</div>
<div class="when" style="left:759px;top:2992px;width:121px">Within a month</div>
<div class="when" style="left:895px;top:2992px;width:122px">1 to 3 months</div>
<div class="when" style="left:622px;top:3058px;width:122px">3 to 6 months</div>
<div class="when" style="left:759px;top:3058px;width:121px">6+ months</div>
<p class="small" style="left:622px;top:3120px;width:390px">By proceeding, you agree to receive the quote by email, have read and understood our <b style="color:var(--ink);text-decoration:underline">Privacy Policy</b> and agree to deedmarkhub.com.au <b style="color:var(--ink);text-decoration:underline">Terms of Use.</b></p>
<span class="abs" style="left:622px;top:3183px;font-size:11px;font-weight:700;color:var(--blue);text-decoration:underline">SUBMIT</span>

<p class="abs" style="left:0;top:3283px;width:1200px;text-align:center;color:var(--blue-mid);font-size:17px;font-weight:600">Testimonials</p>
<h2 class="head sec-title" style="top:3310px">What our clients say</h2>
<div class="arrow" style="left:1034px;background:var(--navy)"><svg width="10" height="10" viewBox="0 0 10 10" fill="none" stroke="#fff" stroke-width="1.6"><path d="M7 1L3 5l4 4"/></svg></div>
<div class="arrow" style="left:1076px;background:var(--blue)"><svg width="10" height="10" viewBox="0 0 10 10" fill="none" stroke="#fff" stroke-width="1.6"><path d="M3 1l4 4-4 4"/></svg></div>
<div class="avatar" style="left:445px;top:3391px;width:75px;height:76px" role="img" aria-label="Client portrait"></div>
<div class="abs" style="left:541px;top:3372px;width:113px;height:113px;border:1px solid #c8ccd3;padding:6px"><div class="avatar" style="position:relative;width:100%;height:100%" role="img" aria-label="Client portrait"></div></div>
<div class="avatar" style="left:678px;top:3391px;width:76px;height:76px;background:linear-gradient(160deg,#dfe2e6,#6c7480)" role="img" aria-label="Client portrait"></div>
<span class="abs" style="left:80px;top:3380px;font-family:Georgia,serif;font-size:330px;line-height:1;color:var(--blue-mist)">&ldquo;</span>
<p class="abs" style="left:0;top:3518px;width:1200px;text-align:center;font-size:14.5px;line-height:22px;color:var(--text)">Thanks Marcus stress free conveyancing service over the Xmas/ New year break.I would definitely<br>recommend Marcus and his team. Third time with Marcus and his team...</p>
<svg class="abs" style="left:542px;top:3582px" width="114" height="22" viewBox="0 0 114 22">
  <g fill="#f5b800">
    <path id="star" d="M11 1l3 6.5 7 .8-5.2 4.8 1.4 7-6.2-3.5-6.2 3.5 1.4-7L1 8.3l7-.8z"/>
    <use href="#star" x="23"/><use href="#star" x="46"/><use href="#star" x="69"/><use href="#star" x="92"/>
  </g>
</svg>
<div class="rule" style="top:3661px;left:70px;width:1060px"></div>

<h2 class="head sec-title" style="top:3727px">From the blog</h2>
<article class="post" style="left:151px">
  <div class="ph" style="background:linear-gradient(160deg,#f2f2f2,#8e8f93)" role="img" aria-label="Hand signing a contract"></div>
  <h4>The ultimate guide to joint<br>venture agreements</h4>
  <p>A joint venture agreement, also known as a JV agreement or development agreement, is one of the most...</p>
  <div class="go"><svg width="10" height="10" viewBox="0 0 10 10" fill="none" stroke="#fff" stroke-width="1.6"><path d="M3 1l4 4-4 4"/></svg></div>
</article>
<article class="post" style="left:456px">
  <div class="ph" style="background:linear-gradient(160deg,#d5d7da,#4c4f55)" role="img" aria-label="Laptop and documents on a desk"></div>
  <h4>The basics of joint venture<br>agreements</h4>
  <p>Looking at commencing or sourcing funding for a property development? A joint venture (JV) can be an...</p>
  <div class="go"><svg width="10" height="10" viewBox="0 0 10 10" fill="none" stroke="#fff" stroke-width="1.6"><path d="M3 1l4 4-4 4"/></svg></div>
</article>
<article class="post" style="left:759px">
  <div class="ph" style="background:linear-gradient(160deg,#3a2c26,#b5612c 55%,#1d1a1a)" role="img" aria-label="Glowing dollar signs on a dark background"></div>
  <h4>Guide to<br>vendor finance</h4>
  <p>With bank lending criteria becoming tighter and tighter, it is becoming increasingly common...</p>
  <div class="go"><svg width="10" height="10" viewBox="0 0 10 10" fill="none" stroke="#fff" stroke-width="1.6"><path d="M3 1l4 4-4 4"/></svg></div>
</article>
<span class="abs" style="left:0;top:4224px;width:1200px;text-align:center;font-size:11px;font-weight:700;color:var(--blue);text-decoration:underline">VIEW ALL BLOGS</span>

<footer class="footer">
  <div class="abs" style="left:119px;top:123px;width:177px;height:170px;display:flex;align-items:center;gap:10px">
    <span style="flex:0 0 14px;height:14px;border-radius:50%;background:var(--blue-soft)"></span>
    <span style="font-size:15px;font-weight:600;color:#fff;line-height:1.4">Harbourline<br>Title Legal</span>
  </div>
  <h4 class="foot-h" style="left:377px;top:121px">Useful links</h4>
  <ul class="foot-list" style="left:377px;top:154px"><li>Home</li><li>Services</li><li>Special Conditions</li><li>Blog Articles</li><li>About Us</li><li>Contact Us</li></ul>
  <h4 class="foot-h" style="left:576px;top:121px">Contact info</h4>
  <div class="abs" style="left:576px;top:158px;width:330px;font-size:12px;line-height:19px;color:#d7dbe2">
    <div style="display:flex;gap:10px"><svg width="14" height="14" viewBox="0 0 14 14" style="flex:0 0 14px"><rect x="1" y="3" width="12" height="9" fill="#7badd7"/><path d="M1 3l6 5 6-5" stroke="#192330" fill="none"/></svg><span>Email:<br>mail@harbourlinetitlelegal.com.au</span></div>
    <div style="display:flex;gap:10px;margin-top:18px"><svg width="14" height="14" viewBox="0 0 24 24" style="flex:0 0 14px"><path fill="#7badd7" d="M6.6 10.8a15 15 0 006.6 6.6l2.2-2.2a1 1 0 011-.25 11 11 0 003.5.55 1 1 0 011 1V20a1 1 0 01-1 1A17 17 0 013 4a1 1 0 011-1h3.5a1 1 0 011 1 11 11 0 00.55 3.5 1 1 0 01-.25 1z"/></svg><span>Phone:<br>(07) 3100 4820</span></div>
    <div style="display:flex;gap:10px;margin-top:18px"><svg width="14" height="16" viewBox="0 0 24 24" style="flex:0 0 14px"><path fill="#7badd7" d="M12 2a7 7 0 017 7c0 5-7 13-7 13S5 14 5 9a7 7 0 017-7zm0 4.5A2.5 2.5 0 1012 11.5 2.5 2.5 0 0012 6.5z"/></svg><span>Location:<br>Level 2, Kestrel House, 18 Kestrel<br>Street, Northvale,<br>Queensland 4099</span></div>
  </div>
  <h4 class="foot-h" style="left:934px;top:121px">Services</h4>
  <ul class="foot-list" style="left:934px;top:154px"><li>Property Development</li><li>Conveyancing</li><li>JV Agreements</li></ul>
  <h4 class="foot-h" style="left:934px;top:262px">Follow us</h4>
  <span class="abs" style="left:934px;top:297px;width:26px;height:26px;border-radius:50%;background:var(--blue-mid)"></span>
  <span class="abs" style="left:969px;top:297px;width:26px;height:26px;border-radius:50%;background:var(--blue-mid)"></span>
  <p class="abs" style="left:0;top:426px;width:1200px;text-align:center;font-size:10.5px;color:#d7dbe2">© Copyright 2025 | All Rights Reserved</p>
  <div class="abs" style="left:1136px;top:387px;width:47px;height:47px;border-radius:50%;background:var(--blue-mid);display:flex;align-items:center;justify-content:center"><svg width="14" height="14" viewBox="0 0 14 14" fill="none" stroke="#fff" stroke-width="1.8"><path d="M2 9l5-5 5 5"/></svg></div>
</footer>

<div class="cta">
  <h3 class="abs head" style="left:45px;top:42px;font-size:40px;color:#fff;font-weight:500;letter-spacing:1px">Need assistance? Please</h3>
  <div class="abs" style="left:674px;top:30px;width:72px;height:72px;background:#fff;display:flex;align-items:center;justify-content:center"><svg width="32" height="32" viewBox="0 0 24 24"><path fill="#192330" d="M6.6 10.8a15 15 0 006.6 6.6l2.2-2.2a1 1 0 011-.25 11 11 0 003.5.55 1 1 0 011 1V20a1 1 0 01-1 1A17 17 0 013 4a1 1 0 011-1h3.5a1 1 0 011 1 11 11 0 00.55 3.5 1 1 0 01-.25 1z"/></svg></div>
  <span class="abs" style="left:769px;top:36px;color:#fff;font-family:'Barlow Semi Condensed',sans-serif;font-size:17px">CALL US</span>
  <span class="abs" style="left:769px;top:58px;color:#fff;font-family:'Barlow Semi Condensed',sans-serif;font-size:29px;font-weight:500">(07) 3100 4820</span>
</div>

</body>
</html>
```